Webdesign für Zahnarztpraxis
Zielgruppe
Zahnarztpraxis
Aufgabenstellung
- Klares und übersichtliches Desgin
- Nicht zu verspielt
- Informativ
- Leichte Naviagtion
- Das Design der alten Webseite soll NICHT kopiert werden
- Die Farben Blau und Grün aus dem Logo sollen sich wiederfinden
- Designbeispiele, die dem Kunden gefallen sind https://www.kolbeck-mirowski-zahnarztpraxis.de/ und https://www.praxisolwing.de/

```html
<!DOCTYPE html>
<html lang="en">
<head>
<meta charset="utf-8">
<title>Zahnhaus Auental – Dental Practice</title>
<link href="https://fonts.googleapis.com/css2?family=Poppins:wght@400;500;600;700;800&display=swap" rel="stylesheet">
<style>
:root{
  --blue:#1e98d6;
  --blue-light:#53b3e3;
  --green:#6cb33f;
  --navy:#0f2150;
  --ink:#1c1c1c;
  --grey:#a9adb3;
  --line:#e8ecef;
  --white:#ffffff;
}
*{box-sizing:border-box;margin:0;padding:0}
html,body{width:1200px;height:4613px;overflow:hidden;background:var(--white)}
body{position:relative;font-family:'Poppins',sans-serif;color:var(--ink)}
.abs{position:absolute}
.brand{display:flex;align-items:center;gap:12px;font-weight:600;font-size:26px;color:var(--blue);white-space:nowrap}
.brand-dot{width:34px;height:34px;border-radius:50%;background:var(--blue)}
.nav{top:44px;right:50px;display:flex;gap:18px;font-size:13px;color:#555}
.nav a{color:inherit;text-decoration:none}
.nav a.active{color:var(--blue);font-weight:500}
.hero-title{left:48px;top:140px;font-size:74px;line-height:74px;font-weight:800;color:var(--navy);letter-spacing:-1px}
.hero-text{left:48px;top:302px;width:300px;font-size:13px;line-height:22px;color:#333}
.btn{display:inline-flex;align-items:center;justify-content:center;border-radius:22px;font-size:12px;font-weight:600;color:var(--white);height:44px}
.btn-blue{background:var(--blue)}
.btn-green{background:var(--green)}
.btn-white{background:var(--white);color:var(--navy);border-radius:12px}
.partners{top:755px;left:134px;width:917px;display:flex;justify-content:space-between;font-size:21px;font-weight:600;color:#b9bcc1}
.panel{left:48px;width:1102px;border-radius:54px;background:var(--blue);overflow:hidden}
.section-title{font-size:46px;font-weight:600;color:var(--white);text-align:center;width:100%}
.card{width:300px;height:300px;border-radius:22px;background:rgba(255,255,255,.22);padding:0 40px;color:var(--white)}
.card.featured{background:var(--white);color:var(--navy)}
.card .more{position:absolute;right:26px;top:26px;font-size:13px;font-weight:500}
.card.featured .more{color:var(--green)}
.card .icon{position:absolute;left:38px;top:34px;width:88px;height:88px;border-radius:50%;background:rgba(255,255,255,.3);display:flex;align-items:center;justify-content:center}
.card.featured .icon{background:var(--green)}
.card h3{position:absolute;left:40px;top:170px;font-size:19px;line-height:24px;font-weight:700}
.card p{position:absolute;left:40px;top:234px;width:220px;font-size:13px;line-height:17px;opacity:.9}
.card.featured p{color:#222;opacity:1}
.practice-title{left:693px;top:2120px;font-size:46px;font-weight:700;color:var(--navy)}
.practice-text{left:696px;top:2196px;width:420px;font-size:13px;line-height:22px;color:#333}
.member{width:300px}
.member .photo{width:300px;height:355px;border-radius:22px;background:
  radial-gradient(ellipse 38% 30% at 50% 18%,#d9b98a 0%,rgba(217,185,138,0) 100%),
  radial-gradient(ellipse 55% 45% at 50% 85%,#e4ecf6 0%,rgba(228,236,246,0) 100%),
  linear-gradient(180deg,#f7f9fb 0%,#eef3f9 50%,#dbe6f2 100%)}
.member .name{margin-top:36px;text-align:center;font-size:19px;font-weight:600;color:var(--white)}
.member .role{margin-top:4px;text-align:center;font-size:13px;color:rgba(255,255,255,.85)}
.arrow{width:43px;height:43px;border-radius:50%;border:2px solid var(--white);display:flex;align-items:center;justify-content:center}
.arrow.dark{border-color:var(--blue)}
.testi-title{left:59px;top:3556px;font-size:48px;font-weight:600;color:#111}
.testi-intro{left:636px;top:3550px;width:515px;font-size:13px;line-height:23px;color:#333}
.quote{width:349px;height:248px;border-radius:22px;background:var(--white);border:1px solid var(--line);box-shadow:0 8px 0 #eef0f2;padding:38px 40px}
.quote.featured{background:var(--green);border-color:var(--green);color:var(--white)}
.stars{font-size:26px;letter-spacing:3px;color:var(--blue)}
.quote.featured .stars{color:var(--white)}
.mark{position:absolute;right:24px;top:14px;font-size:64px;font-weight:800;font-style:italic;color:var(--blue);line-height:1}
.quote.featured .mark{color:var(--white)}
.quote p{margin-top:12px;font-size:13px;line-height:22px}
.quote .sig{position:absolute;right:26px;bottom:28px;font-size:17px;font-weight:700}
.foot-h{font-size:18px;font-weight:600;color:var(--navy)}
.hours{font-size:13px;color:#222;line-height:31px}
.hours td{padding:0;vertical-align:top}
.contact{left:68px;font-size:13px;color:#222;display:flex;align-items:center;gap:12px}
.social{width:37px;height:37px;border-radius:50%;border:2px solid var(--blue);display:flex;align-items:center;justify-content:center}
.social.filled{background:var(--blue)}
.social i{display:block;width:11px;height:11px;border-radius:2px;background:var(--blue)}
.social.filled i{background:var(--white)}
</style>
</head>
<body>

<!-- Header -->
<div class="abs brand" style="left:50px;top:30px"><span class="brand-dot"></span>Zahnhaus Auental</div>
<nav class="abs nav">
  <a class="active" href="#">Home</a><a href="#">Our Practice</a><a href="#">In-House Laboratory</a><a href="#">Our Services</a><a href="#">Our Team</a>
</nav>

<!-- Hero -->
<h1 class="abs hero-title">Dental<br>Practice</h1>
<p class="abs hero-text">Lorem Ipsum is simply dummy text of the printing and typesetting industry.</p>
<a class="abs btn btn-blue" style="left:48px;top:364px;width:124px">Get Directions</a>
<a class="abs btn btn-green" style="left:188px;top:364px;width:122px">View More</a>
<svg class="abs" style="left:0;top:0" width="1200" height="700" role="img" aria-label="Photo of a dentist treating a smiling patient in the dental chair">
  <defs>
    <linearGradient id="heroG" x1="0" y1="0" x2="1" y2="1">
      <stop offset="0" stop-color="#4e6470"/><stop offset=".35" stop-color="#8fb3b8"/><stop offset=".7" stop-color="#b6d3d3"/><stop offset="1" stop-color="#d3e2e4"/>
    </linearGradient>
    <radialGradient id="heroWarm" cx=".42" cy=".55" r=".35">
      <stop offset="0" stop-color="#c99a7e" stop-opacity=".55"/><stop offset="1" stop-color="#c99a7e" stop-opacity="0"/>
    </radialGradient>
    <radialGradient id="heroTeal" cx=".6" cy=".75" r=".4">
      <stop offset="0" stop-color="#7fc4c0" stop-opacity=".6"/><stop offset="1" stop-color="#7fc4c0" stop-opacity="0"/>
    </radialGradient>
  </defs>
  <path id="heroShape" d="M535 111H1110A40 40 0 0 1 1150 151V456A40 40 0 0 1 1110 496H1030A40 40 0 0 0 990 536V617A40 40 0 0 1 950 657H273A40 40 0 0 1 233 617V496A40 40 0 0 1 273 456H455A40 40 0 0 0 495 416V151A40 40 0 0 1 535 111Z" fill="url(#heroG)"/>
  <path d="M535 111H1110A40 40 0 0 1 1150 151V456A40 40 0 0 1 1110 496H1030A40 40 0 0 0 990 536V617A40 40 0 0 1 950 657H273A40 40 0 0 1 233 617V496A40 40 0 0 1 273 456H455A40 40 0 0 0 495 416V151A40 40 0 0 1 535 111Z" fill="url(#heroWarm)"/>
  <path d="M535 111H1110A40 40 0 0 1 1150 151V456A40 40 0 0 1 1110 496H1030A40 40 0 0 0 990 536V617A40 40 0 0 1 950 657H273A40 40 0 0 1 233 617V496A40 40 0 0 1 273 456H455A40 40 0 0 0 495 416V151A40 40 0 0 1 535 111Z" fill="url(#heroTeal)"/>
  <circle cx="1075" cy="580" r="46" fill="var(--blue)"/>
</svg>

<!-- Partners -->
<div class="abs partners"><span>Vitaro</span><span>Medora</span><span>Kestrel</span><span>Plantis</span><span>Calden</span><span>Labrix</span></div>

<!-- Services -->
<section class="abs panel" style="top:888px;height:962px">
  <h2 class="abs section-title" style="top:64px">Our Services</h2>
</section>
<div class="abs card featured" style="left:131px;top:1073px">
  <span class="more">View More</span>
  <div class="icon"><svg width="40" height="40" viewBox="0 0 40 40" fill="none" stroke="#fff" stroke-width="3" stroke-linejoin="round"><rect x="6" y="6" width="28" height="22" rx="3"/><path d="M20 11v12M14 17h12M4 34h32"/></svg></div>
  <h3>Dental<br>Diagnostics</h3>
  <p>Lorem Ipsum is simply dummy text of the printing</p>
</div>
<div class="abs card" style="left:450px;top:1073px">
  <span class="more">View More</span>
  <div class="icon"><svg width="40" height="40" viewBox="0 0 40 40" fill="none" stroke="#fff" stroke-width="3" stroke-linecap="round"><path d="M8 12c8-4 16-4 24 0v10c0 6-6 10-12 10S8 28 8 22z"/><path d="M14 18h12M14 24h12M8 16H4v6l4 2M32 16h4v6l-4 2"/></svg></div>
  <h3>Individual<br>Prophylaxis</h3>
  <p>Lorem Ipsum is simply dummy text of the printing</p>
</div>
<div class="abs card" style="left:768px;top:1073px">
  <span class="more">View More</span>
  <div class="icon"><svg width="40" height="40" viewBox="0 0 40 40" stroke="#fff" stroke-width="6" stroke-linecap="round"><path d="M20 6v28M8 13l24 14M32 13L8 27"/></svg></div>
  <h3>Professional Tooth<br>Cleaning</h3>
  <p>Lorem Ipsum is simply dummy text of the printing</p>
</div>
<div class="abs card" style="left:131px;top:1393px">
  <span class="more">View More</span>
  <div class="icon"><svg width="40" height="40" viewBox="0 0 40 40" fill="none" stroke="#fff" stroke-width="3" stroke-linejoin="round"><path d="M10 4h14l8 8v24H10z"/><path d="M24 4v8h8M13 24h5l2-5 3 9 2-4h4"/></svg></div>
  <h3>Conservative<br>Dentistry</h3>
  <p>Lorem Ipsum is simply dummy text of the printing</p>
</div>
<div class="abs card" style="left:450px;top:1393px">
  <span class="more">View More</span>
  <div class="icon"><svg width="40" height="40" viewBox="0 0 40 40" fill="#fff"><rect x="16" y="2" width="8" height="6" rx="1"/><rect x="18" y="8" width="4" height="5"/><rect x="9" y="13" width="22" height="25" rx="5"/><path d="M18 20h4v5h5v4h-5v5h-4v-5h-5v-4h5z" fill="#7cc5ea"/></svg></div>
  <h3>Dental<br>Prosthetics</h3>
  <p>Lorem Ipsum is simply dummy text of the printing</p>
</div>
<div class="abs card" style="left:768px;top:1393px">
  <span class="more">View More</span>
  <div class="icon"><svg width="40" height="40" viewBox="0 0 40 40" fill="none" stroke="#fff" stroke-width="3" stroke-linecap="round"><path d="M26 6l8 8-18 18H8v-8z"/><path d="M20 14l3 3M16 18l3 3M12 22l3 3M8 32l-4 4"/></svg></div>
  <h3 style="top:194px">Orthodontics</h3>
  <p>Lorem Ipsum is simply dummy text of the printing</p>
</div>
<a class="abs btn btn-white" style="left:530px;top:1751px;width:138px">View All Services</a>

<!-- Our Practice -->
<svg class="abs" style="left:0;top:1990px" width="620" height="510" role="img" aria-label="Photo of a modern dental treatment chair from above">
  <defs>
    <linearGradient id="practiceG" x1="0" y1="0" x2="1" y2="1">
      <stop offset="0" stop-color="#6f6158"/><stop offset=".35" stop-color="#9b8d82"/><stop offset=".6" stop-color="#d2d0cc"/><stop offset="1" stop-color="#f0f0ef"/>
    </linearGradient>
    <radialGradient id="practiceLight" cx=".55" cy=".45" r=".35">
      <stop offset="0" stop-color="#f2f2f1" stop-opacity=".8"/><stop offset="1" stop-color="#f2f2f1" stop-opacity="0"/>
    </radialGradient>
  </defs>
  <path d="M88 14H442A40 40 0 0 1 482 54V220A40 40 0 0 0 522 260H560A40 40 0 0 1 600 300V456A40 40 0 0 1 560 496H88A40 40 0 0 1 48 456V54A40 40 0 0 1 88 14Z" fill="url(#practiceG)"/>
  <path d="M88 14H442A40 40 0 0 1 482 54V220A40 40 0 0 0 522 260H560A40 40 0 0 1 600 300V456A40 40 0 0 1 560 496H88A40 40 0 0 1 48 456V54A40 40 0 0 1 88 14Z" fill="url(#practiceLight)"/>
</svg>
<h2 class="abs practice-title">Our Practice</h2>
<p class="abs practice-text">Practice &amp; dental laboratory in Auental. Prevention and individual prophylaxis in every age group! Dentist also speaks fluent English.</p>
<a class="abs btn btn-green" style="left:695px;top:2288px;width:123px">Get Directions</a>

<!-- Team -->
<section class="abs panel" role="img" aria-label="Faded photo of the practice interior behind the team" style="top:2615px;height:827px;background:radial-gradient(ellipse 40% 50% at 15% 60%,rgba(120,170,200,.35) 0%,rgba(120,170,200,0) 100%),radial-gradient(ellipse 35% 45% at 90% 70%,rgba(110,160,195,.3) 0%,rgba(110,160,195,0) 100%),linear-gradient(180deg,#3aa6dc 0%,#2f9ed8 100%)">
  <h2 class="abs section-title" style="top:90px">Our Team</h2>
</section>
<div class="abs member" style="left:131px;top:2853px">
  <div class="photo" role="img" aria-label="Portrait of dentist Lena Hofmann in a white jacket"></div>
  <div class="name">Lena Hofmann</div><div class="role">Dentist</div>
</div>
<div class="abs member" style="left:450px;top:2853px">
  <div class="photo" role="img" aria-label="Portrait of dentist Miriam Kessler in a white jacket"></div>
  <div class="name">Miriam Kessler</div><div class="role">Dentist</div>
</div>
<div class="abs member" style="left:768px;top:2853px">
  <div class="photo" role="img" aria-label="Portrait of dentist Sabine Lorenz in a white jacket"></div>
  <div class="name">Sabine Lorenz</div><div class="role">Dentist</div>
</div>
<div class="abs arrow" style="left:551px;top:3349px"><svg width="22" height="12" viewBox="0 0 22 12" fill="none" stroke="#fff" stroke-width="1.6"><path d="M21 6H2M7 1L2 6l5 5"/></svg></div>
<div class="abs arrow" style="left:605px;top:3349px"><svg width="22" height="12" viewBox="0 0 22 12" fill="none" stroke="#fff" stroke-width="1.6"><path d="M1 6h19M15 1l5 5-5 5"/></svg></div>

<!-- Testimonials -->
<h2 class="abs testi-title">Testimonials</h2>
<p class="abs testi-intro">Lorem Ipsum is simply dummy text of the printing and typesetting industry. Lorem Ipsum has been the industry's standard dummy text ever since the 1500s, when an unknown printer took a galley of type and scrambled it to make a type specimen book.</p>
<div class="abs quote" style="left:59px;top:3723px">
  <span class="mark">”</span><div class="stars">★★★★★</div>
  <p>“Lorem Ipsum is simply dummy text of the printing and typesetting industry. standard dummy text ever sinc.”</p>
  <span class="sig">-J.O.</span>
</div>
<div class="abs quote featured" style="left:425px;top:3723px">
  <span class="mark">”</span><div class="stars">★★★★★</div>
  <p>“Lorem Ipsum is simply dummy text of the printing and typesetting industry. standard dummy text ever sinc.”</p>
  <span class="sig">-A.S.</span>
</div>
<div class="abs quote" style="left:792px;top:3723px">
  <span class="mark">”</span><div class="stars">★★★★★</div>
  <p>“Lorem Ipsum is simply dummy text of the printing and typesetting industry. standard dummy text ever sinc.”</p>
  <span class="sig">-P.Y.</span>
</div>
<div class="abs arrow dark" style="left:551px;top:4045px"><svg width="22" height="12" viewBox="0 0 22 12" fill="none" stroke="#1e98d6" stroke-width="1.6"><path d="M21 6H2M7 1L2 6l5 5"/></svg></div>
<div class="abs arrow dark" style="left:605px;top:4045px"><svg width="22" height="12" viewBox="0 0 22 12" fill="none" stroke="#1e98d6" stroke-width="1.6"><path d="M1 6h19M15 1l5 5-5 5"/></svg></div>

<!-- Footer -->
<div class="abs brand" style="left:68px;top:4196px"><span class="brand-dot"></span>Zahnhaus Auental</div>
<div class="abs contact" style="top:4290px"><svg width="16" height="16" viewBox="0 0 16 16" fill="#6cb33f"><path d="M3 1l3 3-2 2c1 2 3 4 5 5l2-2 3 3-2 3C7 15 1 9 1 3z"/></svg>Telephone: 03722-40718</div>
<div class="abs contact" style="top:4312px"><svg width="16" height="16" viewBox="0 0 16 16" fill="#6cb33f"><rect x="4" y="1" width="8" height="5"/><rect x="1" y="6" width="14" height="8" rx="1"/></svg>Fax: 03722-40719</div>
<div class="abs contact" style="top:4356px"><svg width="16" height="16" viewBox="0 0 16 16" fill="#6cb33f"><rect x="1" y="3" width="14" height="10" rx="1"/><path d="M1 4l7 5 7-5" stroke="#fff" stroke-width="1.4" fill="none"/></svg>Email: info@zahnhaus-auental.de</div>

<h3 class="abs foot-h" style="left:415px;top:4180px">Telephone Hours</h3>
<table class="abs hours" style="left:415px;top:4218px"><tr><td style="width:92px">Monday:</td><td>9:00 a.m. to 3:00 p.m.</td></tr><tr><td>Tuesday:</td><td>9:00 a.m. to 3:00 p.m.</td></tr><tr><td>Wednesday:</td><td>9:00 a.m. to 12:00 p.m.</td></tr></table>

<h3 class="abs foot-h" style="left:727px;top:4180px">Our Opening Times</h3>
<table class="abs hours" style="left:727px;top:4218px"><tr><td style="width:91px">Monday:</td><td>9:00 a.m. to 1:00 p.m. and 2:00 p.m. to 7:00 p.m.</td></tr><tr><td>Tuesday:</td><td>9:00 a.m. to 1:00 p.m. and 2:00 p.m. to 7:00 p.m.</td></tr><tr><td>Wednesday:</td><td>9:00 a.m. to 2:00 p.m.</td></tr><tr><td>Tuesday:</td><td>closed</td></tr><tr><td>Friday:</td><td>9:00 a.m. to 1:00 p.m.</td></tr><tr><td></td><td style="line-height:18px">... and by appointment</td></tr></table>

<div class="abs" style="left:68px;top:4462px;width:1072px;height:1px;background:var(--line)"></div>
<p class="abs" style="left:72px;top:4526px;font-size:13px;color:#222">© 2025 Zahnhaus Auental</p>
<a class="abs social" style="left:1012px;top:4517px" aria-label="Social profile"><i></i></a>
<a class="abs social filled" style="left:1057px;top:4517px" aria-label="Social profile"><i></i></a>
<a class="abs social" style="left:1102px;top:4517px" aria-label="Social profile"><i></i></a>

</body>
</html>
```